Wedding Dried Apple Label / Name Place Card

We are looking for a simple but stylish label to be attached via string to a bag of dried apples from my family's fruit farm. The size of the label we think should be similar to the size of a business card. The packaging will be a plastic bag: 4" x 2" x 6".
We would like it to say something like:
Remy & Jules
Est. Sept 10, 2017
Dried Apple Slices
Product of Dorrance Orchard Co.
________________
(We need a spot to write in the name of the person and a table number)
Our colors are also grey and navy, and would like these colors to be used.
We have uploaded a photo of the plastic bag.
Wedding

```html
<!DOCTYPE html>
<html lang="en">
<head>
<meta charset="utf-8">
<title>Remy &amp; Jules – Dried Apples Tag</title>
<link rel="stylesheet" href="https://fonts.googleapis.com/css2?family=Great+Vibes&family=Oswald:wght@500&family=Playfair+Display:ital,wght@0,400;0,700;1,400&display=swap">
<style>
  :root {
    --backdrop: #eeebe5;
    --paper-grey: #e3e3e1;
    --navy: #0f2236;
    --white: #ffffff;
    --eyelet: #a9abad;
  }
  * { box-sizing: border-box; margin: 0; padding: 0; }
  html, body { width: 1200px; height: 674px; overflow: hidden; }
  body { background: var(--backdrop); position: relative; }

  .tag {
    position: absolute;
    top: 149px;
    width: 262px;
    height: 462px;
    clip-path: polygon(22% 0, 78% 0, 100% 11%, 100% 100%, 0 100%, 0 11%);
    text-align: center;
  }
  .tag--light { left: 157px; background: var(--paper-grey); color: var(--navy); --ink: var(--navy); --badge-fill: var(--navy); --badge-text: var(--white); }
  .tag--navy  { left: 727px; background: var(--navy); color: var(--white); --ink: var(--white); --badge-fill: transparent; --badge-text: var(--white); }

  .tag__eyelet {
    position: absolute; left: 50%; top: 44px;
    width: 50px; height: 50px; margin-left: -25px;
    border-radius: 50%;
    border: 9px solid var(--eyelet);
    background: var(--backdrop);
  }

  .tag__established {
    position: absolute; top: 176px; left: 50%; transform: translateX(-50%);
    width: 148px; padding-bottom: 3px;
    font-family: "Playfair Display", serif; font-size: 13px;
    border-bottom: 1.5px dotted var(--ink);
  }
  .tag__couple {
    position: absolute; top: 210px; left: 0; right: 0;
    font-family: "Great Vibes", cursive; font-size: 44px; line-height: 1;
  }
  .tag__product {
    position: absolute; top: 282px; left: 20px; right: 20px;
    border-top: 1.5px solid var(--ink);
    border-bottom: 1.5px solid var(--ink);
    padding: 4px 0 3px;
    font-family: "Oswald", sans-serif; font-weight: 500;
    font-size: 23px; letter-spacing: 1px; line-height: 1.2;
  }
  .tag__origin {
    position: absolute; top: 327px; left: 0; right: 0;
    font-family: "Playfair Display", serif; font-style: italic; font-size: 9px;
  }
  .tag__table {
    position: absolute; top: 488px; left: 50%;
  }
  .tag__table-badge {
    position: absolute; top: 348px; left: 50%;
    width: 52px; height: 52px; margin-left: -26px;
    border-radius: 50%;
    border: 1.5px dotted var(--ink);
    padding: 3px;
  }
  .tag__table-number {
    width: 100%; height: 100%; border-radius: 50%;
    background: var(--badge-fill);
    color: var(--badge-text);
    font-family: "Playfair Display", serif; font-weight: 700;
    font-size: 30px; line-height: 44px;
  }
  .tag--navy .tag__table-badge { border-style: dashed; padding: 0; }

  .tag__guest {
    position: absolute; top: 408px; left: 50%; transform: translateX(-50%);
    width: 110px; padding-bottom: 2px;
    font-family: "Great Vibes", cursive; font-size: 24px; line-height: 1.1;
    border-bottom: 1.5px dashed var(--ink);
  }
</style>
</head>
<body>
  <article class="tag tag--light">
    <span class="tag__eyelet"></span>
    <p class="tag__established">est. September 10, 2017</p>
    <h1 class="tag__couple">Remy &amp; Jules</h1>
    <h2 class="tag__product">DRIED APPLES</h2>
    <p class="tag__origin">Product of Dorrance Orchard Co.</p>
    <div class="tag__table-badge"><div class="tag__table-number">3</div></div>
    <p class="tag__guest">Clara</p>
  </article>

  <article class="tag tag--navy">
    <span class="tag__eyelet"></span>
    <p class="tag__established">est. September 10, 2017</p>
    <h1 class="tag__couple">Remy &amp; Jules</h1>
    <h2 class="tag__product">DRIED APPLES</h2>
    <p class="tag__origin">Product of Dorrance Orchard Co.</p>
    <div class="tag__table-badge"><div class="tag__table-number">3</div></div>
    <p class="tag__guest">Clara</p>
  </article>
</body>
</html>
```